Property risk and finance brokerage company needs a business card design

Tarlow Financial requires a business card design. Please integrate existing logo (refer uploaded file).
hex codes used on logo #002649 #008ED6 #444F51 #ADAFAA
font used - Cinzel
Contact information
Renata Sollisford
Director
Mobile: 0491 738 205
email: r.sollisford@tarlowfinancial.example.au
website: www.tarlowfinancial.example.au
CRN : 918354
PO Box 527
Marlowe Vale, Victoria, 3199
Horizontal orientation please
Finance

```html
<!DOCTYPE html>
<html lang="en">
<head>
<meta charset="utf-8">
<title>Tarlow Financial – Business Card</title>
<link href="https://fonts.googleapis.com/css2?family=Tinos:ital,wght@0,400;0,700;1,400&display=swap" rel="stylesheet">
<style>
  :root {
    --backdrop: #a4a4a4;
    --card: #f1f1ef;
    --navy-deep: #12375a;
    --navy-mid: #22557f;
    --navy-light: #3a77a6;
    --rule: rgba(230, 236, 242, 0.85);
    --text-light: #eef2f6;
    --text-muted: #9fb3c6;
    --brand-blue: #1f5a86;
  }
  * { box-sizing: border-box; margin: 0; padding: 0; }
  html, body {
    width: 1200px; height: 1000px; overflow: hidden;
    background: var(--backdrop);
    font-family: "Tinos", "Times New Roman", serif;
  }
  .sheet {
    position: relative; width: 1200px; height: 1000px;
    display: flex; flex-direction: column; align-items: center; justify-content: center; gap: 60px;
  }
  .card {
    position: relative; width: 700px; height: 400px;
    background: var(--card); overflow: hidden;
    box-shadow: 0 8px 22px rgba(0,0,0,0.22);
  }
  .panel {
    position: absolute;
    background: linear-gradient(160deg, var(--navy-light) 0%, var(--navy-mid) 40%, var(--navy-deep) 100%);
  }
  .panel::after {
    content: ""; position: absolute; inset: 6px;
    border: 1.5px solid var(--rule); border-radius: inherit;
  }
  /* Front: centred stadium with brand name */
  .card--front .panel {
    left: 52px; right: 52px; top: 54px; bottom: 54px; border-radius: 146px;
    display: flex; align-items: center; justify-content: center; gap: 18px;
  }
  .brand { display: flex; align-items: center; gap: 16px; }
  .brand__dot { width: 48px; height: 48px; border-radius: 50%; }
  .brand__name {
    font-weight: 400; text-transform: uppercase; letter-spacing: 1px;
    font-size: 34px; line-height: 1.02;
  }
  .card--front .brand__dot { background: var(--text-light); }
  .card--front .brand__name { color: var(--text-light); }
  /* Back: contact panel bleeding off the left edge */
  .card--back .panel {
    left: -40px; width: 448px; top: 34px; bottom: 34px; border-radius: 0 166px 166px 0;
  }
  .contact { position: absolute; left: 34px; top: 66px; width: 340px; color: var(--text-light); z-index: 1; }
  .contact__name { font-weight: 700; font-size: 20px; }
  .contact__title { font-style: italic; font-size: 16px; color: var(--text-muted); margin-top: 2px; }
  .contact__rule { height: 2px; background: var(--rule); width: 320px; margin: 12px 0 30px; }
  .contact__line { font-size: 18px; line-height: 27px; white-space: nowrap; }
  .contact__label { font-style: italic; color: var(--text-muted); }
  .contact__address { margin-top: 14px; }
  .card--back .brand { position: absolute; left: 440px; top: 168px; }
  .card--back .brand__dot { background: var(--brand-blue); }
  .card--back .brand__name { color: var(--brand-blue); font-size: 28px; }
</style>
</head>
<body>
<main class="sheet">
  <section class="card card--front" aria-label="Business card front">
    <div class="panel">
      <div class="brand">
        <span class="brand__dot"></span>
        <span class="brand__name">Tarlow<br>Financial</span>
      </div>
    </div>
  </section>

  <section class="card card--back" aria-label="Business card back">
    <div class="panel"></div>
    <div class="contact">
      <p class="contact__name">Renata Sollisford</p>
      <p class="contact__title">Managing Director</p>
      <div class="contact__rule"></div>
      <p class="contact__line"><span class="contact__label">m:</span> 0491 738 205</p>
      <p class="contact__line"><span class="contact__label">e:</span> r.sollisford@tarlowfinancial.example.au</p>
      <p class="contact__line"><span class="contact__label">Credit Rep No.:</span> nnn nnn nnn</p>
      <div class="contact__address">
        <p class="contact__line">PO Box 527</p>
        <p class="contact__line">Marlowe Vale, Victoria, 3199</p>
      </div>
    </div>
    <div class="brand">
      <span class="brand__dot"></span>
      <span class="brand__name">Tarlow<br>Financial</span>
    </div>
  </section>
</main>
</body>
</html>
```